依頼詳細
写真・ビデオの撮影・編集および写真スタジオを行っています。お客様にお送りする封筒のデザインをお願いします。かっこよく・爽やかなイメージでお願いします。封筒の下位置部分のレイアウトでお願いします。。
記載項目
法人名/住所/電話/Fax/ホームページアドレス+ロゴ
希望イメージ
シンプル 複雑
単色 カラフル
暗い 明るい
日常 高級
遊び心 厳粛
未来的 伝統的
女性的 男性的
希望する色
青系、水色系、緑系
納品ファイル
• フォトショップ形式 (.psd)
補足説明
素材のロゴデータのロゴ部分と文字部分のバランスはおまかせ致します。
封筒の色は白色で考えております。よろしくお願い致します。

```html
<!DOCTYPE html>
<html lang="ja">
<head>
<meta charset="UTF-8">
<title>LUMINA Envelope</title>
<link href="https://fonts.googleapis.com/css2?family=Noto+Sans+JP:wght@400;500&display=swap" rel="stylesheet">
<style>
  :root {
    --paper: #ffffff;
    --page-bg: #ffffff;
    --outline: #c9c9c9;
    --box-line: #8a8a8a;
    --brand-blue: #2f6db3;
    --wordmark-grey: #a9a9a9;
    --ink: #333333;
  }
  html, body {
    margin: 0;
    padding: 0;
    width: 846px;
    height: 1200px;
    overflow: hidden;
    background: var(--page-bg);
  }
  .canvas {
    position: relative;
    width: 846px;
    height: 1200px;
    font-family: "Noto Sans JP", sans-serif;
  }
  .envelope-shape {
    position: absolute;
    inset: 0;
  }
  .postal-boxes {
    position: absolute;
    left: 480px;
    top: 262px;
    display: flex;
    align-items: center;
    gap: 4px;
  }
  .postal-box {
    width: 24px;
    height: 30px;
    border: 1.5px solid var(--box-line);
    box-sizing: border-box;
    background: var(--paper);
  }
  .postal-dash {
    width: 8px;
    height: 1.5px;
    background: var(--box-line);
    margin: 0 1px;
  }
  .vertical-name {
    position: absolute;
    left: 700px;
    top: 690px;
    transform: translate(-50%, -50%) rotate(-90deg);
    font-family: "Noto Sans JP", sans-serif;
    font-weight: 500;
    font-size: 104px;
    letter-spacing: 14px;
    color: var(--wordmark-grey);
    white-space: nowrap;
    line-height: 1;
  }
  .brand-mark {
    position: absolute;
    left: 121px;
    top: 958px;
    display: flex;
    align-items: center;
    gap: 12px;
  }
  .brand-square {
    width: 30px;
    height: 30px;
    background: var(--brand-blue);
  }
  .brand-name {
    font-family: "Noto Sans JP", sans-serif;
    font-weight: 500;
    font-size: 32px;
    color: var(--brand-blue);
    line-height: 1;
    letter-spacing: 1px;
  }
  .sender-info {
    position: absolute;
    left: 340px;
    top: 912px;
    font-size: 14px;
    line-height: 27px;
    color: var(--ink);
  }
  .sender-info p { margin: 0; white-space: nowrap; }
  .sender-info .gap { margin-left: 12px; }
</style>
</head>
<body>
<div class="canvas">
  <svg class="envelope-shape" width="846" height="1200" viewBox="0 0 846 1200">
    <polygon class="envelope-flap" points="85,155 104,60 742,60 762,155"
             fill="var(--paper)" stroke="var(--outline)" stroke-width="1.5" stroke-linejoin="round"/>
    <rect class="envelope-body" x="85" y="155" width="677" height="1002"
          fill="var(--paper)" stroke="var(--outline)" stroke-width="1.5"/>
  </svg>

  <div class="postal-boxes" aria-label="郵便番号欄">
    <span class="postal-box"></span>
    <span class="postal-box"></span>
    <span class="postal-box"></span>
    <span class="postal-dash"></span>
    <span class="postal-box"></span>
    <span class="postal-box"></span>
    <span class="postal-box"></span>
    <span class="postal-box"></span>
  </div>

  <div class="vertical-name">LUMINA</div>

  <div class="brand-mark">
    <span class="brand-square"></span>
    <span class="brand-name">LUMINA</span>
  </div>

  <div class="sender-info">
    <p class="company">株式会社ルミナ</p>
    <p class="postcode">〒123-456</p>
    <p class="address">XX県XX市XXXXXXXX</p>
    <p class="phone">TEL 00-0000-0000<span class="gap">FAX 00-0000-0000</span></p>
    <p class="web">URL https://www.lumina-studio.jp</p>
  </div>
</div>
</body>
</html>
```